Antigen Preservation Center

The company will provide a contract research services to stabilize various viruses, viral vectors, and vaccines. It may offer some licensing opportunities for stabilizing technologies. Main area of applications are pharmaceutical, therapeutic, and vaccination field. The company aspires to develop room temperature vaccines for global distribution beyond the current cold chain.
Updates

Target Market(s)

pharmaceutical, therapeutic and vaccination fields

Coding

Number of Pages Required

4 page

Requirements
Must have
• Incorporate a APC logo, attached at the bottom, on the Web page

```html
<!DOCTYPE html>
<html lang="en">
<head>
<meta charset="utf-8">
<title>Antigen Preservation Center</title>
<link href="https://fonts.googleapis.com/css2?family=Poppins:wght@400;500;600&family=Open+Sans:wght@400;600&display=swap" rel="stylesheet">
<style>
:root{
  --navy:#1b2a6b;
  --blue:#0a9ade;
  --blue-dark:#0678b8;
  --text:#444;
  --muted:#666;
  --light:#f4f4f4;
  --card:#f5f5f5;
  --dark:#333;
  --white:#fff;
}
*{margin:0;padding:0;box-sizing:border-box}
html,body{width:1200px;height:3175px;overflow:hidden}
body{position:relative;background:var(--white);font-family:"Open Sans",Arial,sans-serif;color:var(--text)}
.abs{position:absolute}
h2,h3,h4,.nav a,.brand{font-family:"Poppins",Arial,sans-serif;font-weight:400}

/* header */
.header{position:absolute;left:0;top:0;width:1200px;height:88px;background:var(--white)}
.top-tab{position:absolute;left:755px;top:0;width:325px;height:34px;background:var(--blue);border-radius:0 0 18px 18px;display:flex;align-items:center;justify-content:center;gap:26px;color:var(--white);font-size:15px}
.top-tab span{display:flex;align-items:center;gap:7px}
.brand{position:absolute;left:138px;top:22px;color:var(--navy);font-size:22px;line-height:26px;font-weight:500}
.brand small{display:block;font-size:22px;padding-left:110px}
.nav{position:absolute;left:568px;top:58px;display:flex;gap:0}
.nav a{color:var(--navy);font-size:14px;text-decoration:none;width:100px}
.nav a.active{font-weight:600}
.nav a.news{font-size:17px}

/* hero */
.hero{position:absolute;left:0;top:88px;width:1200px;height:537px;background:linear-gradient(180deg,#8d6f86 0%,#c88a8e 22%,#5d5566 45%,#2f2f3a 70%,#1d1b22 100%)}
.hero .arrow{position:absolute;top:255px;width:26px;height:30px;background:rgba(0,0,0,.55);display:flex;align-items:center;justify-content:center}
.hero-caption{position:absolute;left:0;top:455px;width:1200px;text-align:center;color:var(--white);font-family:"Poppins",sans-serif;font-size:25px;line-height:38px}

/* section title */
.sec-title{position:absolute;left:0;width:1200px;text-align:center;color:var(--navy);font-size:21px}
.sec-title::after{content:"";display:block;width:110px;height:2px;background:var(--blue);margin:10px auto 0}
.sec-text{position:absolute;left:210px;width:780px;text-align:center;font-size:12.5px;line-height:23px;color:var(--text)}

/* feature cards */
.card{position:absolute;width:290px;height:212px;background:var(--card);box-shadow:0 2px 8px rgba(0,0,0,.25);text-align:center;padding-top:30px}
.card svg{display:block;margin:0 auto;height:80px}
.card h3{color:var(--blue);font-size:17px;margin-top:6px;font-weight:500}
.card p{font-size:12.5px;line-height:22px;margin:6px 18px 0;color:var(--text)}
.card.active{background:var(--blue)}
.card.active h3,.card.active p{color:var(--white)}

/* about */
.about{position:absolute;left:0;top:1065px;width:1200px;height:425px;background:var(--light)}
.about h2{position:absolute;left:138px;top:62px;font-size:21px;color:var(--navy)}
.about h2 span{color:var(--blue)}
.about h2::after{content:"";display:block;width:80px;height:2px;background:var(--blue);margin-top:8px}
.about p{position:absolute;left:138px;width:430px;font-size:12.5px;line-height:23px}
.btn{position:absolute;background:var(--blue-dark);color:var(--white);font-size:12px;font-weight:600;border-radius:14px;text-align:center}
.video{position:absolute;left:612px;top:97px;width:446px;height:246px;background:#3a3a3a;color:#d8d8d8;font-family:"Poppins",sans-serif;font-size:30px;line-height:34px;text-align:center;padding-top:80px}

/* news */
.news-card{position:absolute;top:1605px;width:283px;height:433px;background:var(--white);border:1px solid #e3e3e3;text-align:center}
.news-img{height:213px}
.date{position:absolute;left:0;top:0;width:50px;background:var(--navy);color:var(--white);font-family:"Poppins",sans-serif;font-size:25px;line-height:32px}
.date small{display:block;background:var(--blue);font-size:9px;line-height:14px}
.news-card h4{font-size:15.5px;line-height:24px;color:#222;margin:16px 20px 0}
.news-card p{font-size:12.5px;line-height:22px;margin:14px 18px 0}
.news-card .more{display:block;margin-top:14px;font-style:italic;font-size:12px;color:var(--navy)}

/* applications */
.apps{position:absolute;left:0;top:2085px;width:1200px;height:463px;background:var(--light)}

/* cta */
.cta{position:absolute;left:155px;top:2606px;width:885px;height:237px;background:var(--light);border-radius:6px;box-shadow:4px 4px 10px rgba(0,0,0,.35);text-align:center;z-index:2}
.cta h2{font-size:21px;color:#222;margin-top:50px}
.cta p{font-size:12.5px;line-height:23px;width:740px;margin:12px auto 0}

/* footer */
.footer{position:absolute;left:0;top:2798px;width:1200px;height:329px;background:var(--dark);color:#eee}
.footer h4{position:absolute;top:110px;font-size:13.5px;color:var(--white)}
.footer h4::after{content:"";display:block;width:38px;height:2px;background:#ccc;margin-top:6px}
.footer ul{position:absolute;list-style:none;font-size:12.5px;line-height:26px}
.contact-row{position:absolute;left:290px;display:flex;gap:18px;font-size:12.5px;line-height:17px}
.map{position:absolute;left:535px;top:152px;width:225px;height:145px;background:linear-gradient(135deg,#eef0f2,#dfe5ea)}
.socials{position:absolute;left:805px;top:150px;display:flex;gap:10px}
.socials span{width:24px;height:24px;border-radius:50%;background:var(--white)}
.foot-brand{position:absolute;left:805px;top:200px;font-family:"Poppins",sans-serif;font-size:22px;line-height:24px;color:var(--white)}
.foot-brand small{display:block;font-size:22px;padding-left:105px}
.bottom-bar{position:absolute;left:0;top:3127px;width:1200px;height:48px;background:var(--blue);color:var(--white);font-size:11px}
.bottom-bar .copy{position:absolute;left:138px;top:16px}
.bottom-bar .links{position:absolute;left:860px;top:21px}
</style>
</head>
<body>

<header class="header">
  <div class="top-tab">
    <span><svg width="18" height="18" viewBox="0 0 24 24"><circle cx="12" cy="12" r="11" fill="none" stroke="#fff" stroke-width="2"/><path d="M8 6l2 3-1 1c1 2 3 4 5 5l1-1 3 2-1 2c-5 0-10-5-10-10z" fill="#fff"/></svg>123.456.7890</span>
    <span><svg width="20" height="14" viewBox="0 0 20 14"><rect x="1" y="1" width="18" height="12" fill="none" stroke="#fff" stroke-width="1.6"/><path d="M1 1l9 7 9-7" fill="none" stroke="#fff" stroke-width="1.6"/></svg>inquiry@apc.com</span>
  </div>
  <div class="brand">Antigen Preservation<small>Center</small></div>
  <nav class="nav">
    <a class="active">Home</a><a>About Us</a><a>Services</a><a class="news">News</a><a>Contact Us</a>
  </nav>
</header>

<section class="hero" role="img" aria-label="City skyline at dusk with highways and lit towers">
  <div class="arrow" style="left:0"><svg width="10" height="12"><path d="M8 1L2 6l6 5" fill="none" stroke="#fff" stroke-width="2"/></svg></div>
  <div class="arrow" style="right:0"><svg width="10" height="12"><path d="M2 1l6 5-6 5" fill="none" stroke="#fff" stroke-width="2"/></svg></div>
  <p class="hero-caption">Lorem Ipsum Dolor Sit Amet Cnsectetuer ing Elit, Sed DiaAdipiscing Elit,<br>Sed Diam Nonumy In USA</p>
</section>

<h2 class="sec-title" style="top:677px">Providing A Contract Research Services To Stabilize Various</h2>
<p class="sec-text" style="top:722px">Lorem ipsum dolor sit amet, consectetuer adipiscing elit, sed diam nonummy nibh euismod tincidunt ut laoreet dolore magna aliquam erat volutpat. Ut wisi enim ad minim veniam, quis nostrud exerci tation ullamcorper.</p>

<div class="card" style="left:138px;top:793px">
  <svg viewBox="0 0 80 80" width="80"><g stroke="#0a9ade" stroke-width="4" fill="#0a9ade"><circle cx="40" cy="40" r="13"/><line x1="40" y1="10" x2="40" y2="70"/><line x1="10" y1="40" x2="70" y2="40"/><line x1="19" y1="19" x2="61" y2="61"/><line x1="61" y1="19" x2="19" y2="61"/><circle cx="40" cy="10" r="4"/><circle cx="40" cy="70" r="4"/><circle cx="10" cy="40" r="4"/><circle cx="70" cy="40" r="4"/><circle cx="19" cy="19" r="4"/><circle cx="61" cy="61" r="4"/><circle cx="61" cy="19" r="4"/><circle cx="19" cy="61" r="4"/></g></svg>
  <h3>Viruses</h3>
  <p>Lorem ipsum dolor sit amet, consectetuer adipiscing elit, sed diam non...</p>
</div>
<div class="card active" style="left:452px;top:793px">
  <svg viewBox="0 0 120 80" width="120"><g stroke="#fff" stroke-width="2" fill="#fff"><circle cx="60" cy="22" r="6"/><line x1="60" y1="22" x2="30" y2="42"/><line x1="60" y1="22" x2="90" y2="42"/><line x1="60" y1="22" x2="60" y2="55"/><circle cx="30" cy="42" r="5"/><circle cx="90" cy="42" r="5"/><circle cx="60" cy="55" r="5"/><line x1="30" y1="42" x2="12" y2="60"/><line x1="90" y1="42" x2="108" y2="60"/><circle cx="12" cy="60" r="3"/><circle cx="108" cy="60" r="3"/><circle cx="20" cy="30" r="3"/><circle cx="100" cy="30" r="3"/></g></svg>
  <h3>Viral Vectors</h3>
  <p>Lorem ipsum dolor sit amet, consectetuer adipiscing elit, sed diam non...</p>
</div>
<div class="card" style="left:762px;top:793px">
  <svg viewBox="0 0 80 80" width="80"><g stroke="#0a9ade" stroke-width="4" fill="none" stroke-linecap="round"><path d="M22 58L52 28l8 8-30 30z"/><line x1="60" y1="20" x2="70" y2="10"/><line x1="52" y1="16" x2="68" y2="32"/><line x1="22" y1="58" x2="10" y2="70"/></g></svg>
  <h3>Vaccines</h3>
  <p>Lorem ipsum dolor sit amet, consectetuer adipiscing elit, sed diam non...</p>
</div>

<section class="about">
  <h2>About Antigen Preservation <span>Center</span></h2>
  <p style="top:110px">Lorem ipsum dolor sit amet, consectetuer adipiscing elit, sed diam nonummy nibh euismod tincidunt ut laoreet dolore magna aliquam erat volutpat. Ut wisi enim ad minim veniam, quis nostrud exerci tation ullamcorper suscipit lobortis nisl ut aliquip ex ea.</p>
  <p style="top:205px">Lit, sed diam nonummy nibh euismod tincidunt ut laoreet dolore mana aliquam erat volutpat. Ut wisi enim ad minim veniam, quis nostrud exerci tation ullamcorper suscipit. nonummy nibh euismod tincidunt ut laoreet.</p>
  <div class="btn" style="left:138px;top:312px;width:105px;height:30px;line-height:30px">Read More</div>
  <div class="video" role="img" aria-label="Introductory video thumbnail">
    Antigen Preservation<br>Center
    <svg class="abs" style="left:200px;top:105px" width="46" height="46" viewBox="0 0 46 46"><circle cx="23" cy="23" r="22" fill="#fff"/><path d="M18 14l14 9-14 9z" fill="#3a3a3a"/></svg>
  </div>
</section>

<h2 class="sec-title" style="top:1549px">Latest News</h2>

<article class="news-card" style="left:138px">
  <div class="news-img" role="img" aria-label="Lab researcher in gloves handling samples" style="background:linear-gradient(135deg,#2c5c8f,#6aa6d6 55%,#cfe2f0)"></div>
  <div class="date">05<small>JAN '19</small></div>
  <h4>Lit, sed diam nonummy niby nib euismod tincidunt ut laoreet.</h4>
  <p>Lorem ipsum dolor sit amet nsectetuer adipiscing elit, sed diam nonummy nibh euismod tincidunt ut laoreet dolore maa aliquam erat volutpat.</p>
  <span class="more">Continue Reading →</span>
</article>
<article class="news-card" style="left:455px">
  <div class="news-img" role="img" aria-label="Vaccine vial with blue cap" style="background:linear-gradient(135deg,#e8eaee,#c7ccd4 60%,#7d8ea8)"></div>
  <div class="date">05<small>JAN '19</small></div>
  <h4>Lit, sed diam nonummy niby nib euismod tincidunt ut laoreet.</h4>
  <p>Lorem ipsum dolor sit amet nsectetuer adipiscing elit, sed diam nonummy nibh euismod tincidunt ut laoreet dolore maa aliquam erat volutpat.</p>
  <span class="more">Continue Reading →</span>
</article>
<article class="news-card" style="left:772px">
  <div class="news-img" role="img" aria-label="Laboratory equipment with bioprocess bag" style="background:linear-gradient(135deg,#4a4f58,#9aa2ac 50%,#e4e8ec)"></div>
  <div class="date">05<small>JAN '19</small></div>
  <h4>Lit, sed diam nonummy niby nib euismod tincidunt ut laoreet.</h4>
  <p>Lorem ipsum dolor sit amet nsectetuer adipiscing elit, sed diam nonummy nibh euismod tincidunt ut laoreet dolore maa aliquam erat volutpat.</p>
  <span class="more">Continue Reading →</span>
</article>

<section class="apps"></section>
<h2 class="sec-title" style="top:2149px">Our Main Area Of Applications Are</h2>
<p class="sec-text" style="top:2192px">Lorem ipsum dolor sit amet, consectetuer adipiscing elit, sed diam nonummy nibh euismod tincidunt ut laoreet dolore magna aliquam erat volutpat. Ut wisi enim ad minim veniam, quis nostrud exerci tation ullamcorper.</p>

<div class="card" style="left:141px;top:2263px">
  <svg viewBox="0 0 80 80" width="80"><g fill="#0a9ade"><rect x="14" y="18" width="22" height="46" rx="11" transform="rotate(-30 25 41)"/><circle cx="54" cy="52" r="16"/></g><line x1="42" y1="62" x2="66" y2="42" stroke="#f5f5f5" stroke-width="3"/></svg>
  <h3>Pharmaceutical</h3>
  <p>Lorem ipsum dolor sit amet, consectetuer adipiscing elit, sed diam non...</p>
</div>
<div class="card active" style="left:455px;top:2263px">
  <svg viewBox="0 0 80 80" width="80"><path d="M40 40C30 32 24 26 24 19a8 8 0 0 1 16-2 8 8 0 0 1 16 2c0 7-6 13-16 21z" fill="#fff"/><g fill="none" stroke="#fff" stroke-width="4" stroke-linecap="round"><path d="M8 30v20l18 18h10"/><path d="M72 30v20L54 68H44"/><path d="M18 46l10 10"/><path d="M62 46L52 56"/></g></svg>
  <h3>Therapeutic</h3>
  <p>Lorem ipsum dolor sit amet, consectetuer adipiscing elit, sed diam non...</p>
</div>
<div class="card" style="left:766px;top:2263px">
  <svg viewBox="0 0 80 80" width="80"><g stroke="#0a9ade" stroke-width="4" fill="none" stroke-linecap="round"><path d="M22 58L52 28l8 8-30 30z"/><line x1="60" y1="20" x2="70" y2="10"/><line x1="52" y1="16" x2="68" y2="32"/><line x1="22" y1="58" x2="10" y2="70"/></g></svg>
  <h3>Vaccination</h3>
  <p>Lorem ipsum dolor sit amet, consectetuer adipiscing elit, sed diam non...</p>
</div>

<section class="cta">
  <h2>Also offering some licensing opportunities for stabilizing technologies.</h2>
  <p>Lorem ipsum dolor sit amet, consectetuer adipiscing elit, sed diam nonummy nibh euismod tincidunt ut laoreet dolore magna aliquam erat volutpat. Ut wisi enim ad minim veniam, quis nostrud exerci tation ullamcorper.</p>
  <div class="btn" style="left:373px;top:146px;width:143px;height:36px;line-height:36px;border-radius:3px;background:var(--blue);font-size:15px;font-weight:400">✆ 123.456.7890</div>
</section>

<footer class="footer">
  <h4 style="left:138px">Quick Links</h4>
  <ul style="left:138px;top:145px"><li>Home</li><li>About Us</li><li>Services</li><li>News</li><li>Contact Us</li></ul>
  <h4 style="left:290px">Contact Details</h4>
  <div class="contact-row" style="top:152px"><svg width="12" height="16" viewBox="0 0 12 16"><path d="M6 0a6 6 0 0 1 6 6c0 4-6 10-6 10S0 10 0 6a6 6 0 0 1 6-6z" fill="#fff"/><circle cx="6" cy="6" r="2" fill="#333"/></svg><span>Antigen Preservation Center<br>Street Name, City<br>Name State Zipcode</span></div>
  <div class="contact-row" style="top:231px"><svg width="14" height="14" viewBox="0 0 24 24"><circle cx="12" cy="12" r="11" fill="none" stroke="#fff" stroke-width="2"/><path d="M8 6l2 3-1 1c1 2 3 4 5 5l1-1 3 2-1 2c-5 0-10-5-10-10z" fill="#fff"/></svg><span>123.456.7890</span></div>
  <div class="contact-row" style="top:263px"><svg width="14" height="11" viewBox="0 0 20 14"><rect x="1" y="1" width="18" height="12" fill="none" stroke="#fff" stroke-width="2"/><path d="M1 1l9 7 9-7" fill="none" stroke="#fff" stroke-width="2"/></svg><span>inquiry@apc.com</span></div>
  <h4 style="left:535px">Location Map</h4>
  <div class="map" role="img" aria-label="Street map showing the office location"></div>
  <h4 style="left:805px">Follow Us On</h4>
  <div class="socials"><span></span><span></span><span></span></div>
  <div class="foot-brand">Antigen Preservation<small>Center</small></div>
</footer>

<div class="bottom-bar">
  <span class="copy">Copyright © 2019 Antigen Preservation Center. All Rights Reserved.</span>
  <span class="links">Terms &amp; Conditions | Privacy Policy</span>
</div>

</body>
</html>
```